HARBORLINE AUTO GLASS

Mobile Glass Shop:

1) Windshield REPAIR 2)Windshield replacment 3) Rear Windshield Replacment 4) Side Window Replacment 5) car window replacment 6) Power Window Repair.

Schedual a service within 24 hour with one of our certified technicians.

See "brightvane auto repair" web site for referance on the nature of our buisness and service. www.brightvane-example.com

```html
<!DOCTYPE html>
<html lang="en">
<head>
<meta charset="utf-8">
<title>Harborline Auto Glass</title>
<link rel="stylesheet" href="https://fonts.googleapis.com/css2?family=Roboto+Condensed:wght@400;700&family=Open+Sans:ital,wght@0,400;0,600;1,400&display=swap">
<style>
:root{
  --blue:#1ea3dc;
  --blue-dark:#1585bd;
  --ink:#111;
  --text:#444;
  --muted:#8a8a8a;
  --soft:#f5f5f5;
  --field:#f1f1f1;
  --footer:#17191c;
  --white:#fff;
  --star:#ffc21a;
}
*{box-sizing:border-box;margin:0;padding:0}
html,body{width:1200px;height:3462px;overflow:hidden}
body{position:relative;font-family:"Open Sans",sans-serif;color:var(--text);background:var(--white)}
.head{font-family:"Roboto Condensed",sans-serif;font-weight:700;color:var(--ink);text-transform:uppercase}
.head span{color:var(--blue)}
.btn{position:absolute;display:flex;align-items:center;justify-content:center;border-radius:30px;background:var(--blue);color:var(--white);font-family:"Roboto Condensed",sans-serif;font-weight:700;font-size:15px}

/* header */
.site-header{position:absolute;left:0;top:0;width:1200px;height:102px;background:var(--white)}
.brand{position:absolute;left:118px;top:32px;display:flex;align-items:center;gap:10px}
.brand-square{width:34px;height:34px;background:var(--blue);border-radius:4px}
.brand-name{font-family:"Roboto Condensed",sans-serif;font-weight:700;font-size:22px;color:var(--blue-dark);line-height:1}
.topbar{position:absolute;left:541px;top:0;width:545px;height:44px;background:var(--blue);border-radius:0 0 22px 22px;display:flex;align-items:center;justify-content:center;gap:26px;color:var(--white);font-size:15px}
.topbar svg{width:15px;height:15px;fill:var(--white);vertical-align:-2px;margin-right:8px}
.nav{position:absolute;top:62px;left:470px;display:flex;gap:54px;font-size:16px;color:#222}
.nav .active{color:var(--blue);position:relative}
.nav .active::after{content:"";position:absolute;left:0;right:0;top:32px;height:3px;background:var(--blue)}

/* hero */
.hero{position:absolute;left:0;top:102px;width:1200px;height:624px}
.hero svg{position:absolute;left:0;top:0}
.hero-title{position:absolute;left:107px;top:178px;font-size:54px;line-height:62px;color:var(--white)}
.hero-text{position:absolute;left:111px;top:306px;width:450px;font-size:15px;line-height:26px;color:var(--white)}
.hero .btn{left:111px;top:375px;width:186px;height:58px;background:var(--white);color:var(--blue)}

/* about */
.about{position:absolute;left:0;top:726px;width:1200px;height:675px}
.about-frame{position:absolute;left:112px;top:56px}
.badge{position:absolute;left:410px;top:474px;width:112px;height:112px;border-radius:50%;background:var(--white);box-shadow:0 4px 16px rgba(0,0,0,.15);display:flex;flex-direction:column;align-items:center;justify-content:center;font-family:"Roboto Condensed",sans-serif;font-weight:700;line-height:1}
.badge b{font-size:44px;color:#222;font-style:italic}
.badge i{font-size:16px;color:var(--blue)}
.about-title{position:absolute;left:537px;top:136px;font-size:36px}
.about-text{position:absolute;left:537px;top:188px;width:553px;font-size:15px;line-height:25.7px}
.about .btn{left:537px;top:461px;width:146px;height:57px}

/* services */
.services{position:absolute;left:0;top:1401px;width:1200px;height:637px;background:var(--soft)}
.services-title{position:absolute;left:0;width:1200px;top:60px;text-align:center;font-size:36px}
.card{position:absolute;top:255px;width:232px;height:286px;background:var(--white);border-radius:14px;box-shadow:0 2px 12px rgba(0,0,0,.06);text-align:center}
.card-pic{position:absolute;left:16px;top:-128px;width:200px;height:258px;clip-path:polygon(20% 0,70% 14%,100% 48%,94% 100%,0 100%,12% 55%)}
.card h3{position:absolute;left:0;right:0;top:145px;font-size:19px;line-height:26px}
.card p{position:absolute;left:18px;right:18px;top:178px;font-size:15px;line-height:26px;height:78px;overflow:hidden}
.card .btn{left:59px;top:270px;width:114px;height:40px;font-size:13px}
.arrow{position:absolute;top:1808px;width:21px;height:21px;border-radius:50%;background:var(--blue)}
.arrow svg{width:21px;height:21px}

/* reviews */
.reviews{position:absolute;left:0;top:2038px;width:1200px;height:394px;background:linear-gradient(100deg,#2fa9dc,#1c98d1 55%,#2eaee0)}
.reviews-title{position:absolute;left:110px;top:52px;font-size:31px;line-height:50px;color:var(--white)}
.reviewer{position:absolute;left:465px;top:62px;font-size:28px;color:var(--white)}
.stars{position:absolute;left:465px;top:104px;display:flex;gap:6px}
.stars svg{width:18px;height:18px;fill:var(--star)}
.quote{position:absolute;left:466px;top:142px;width:610px;font-style:italic;font-size:15.5px;line-height:26px;color:#d8f0fb;text-indent:44px}
.quote-mark{position:absolute;left:466px;top:146px;font-family:Georgia,serif;font-size:48px;line-height:1;color:#1b6f9e;font-weight:700}
.dots{position:absolute;left:465px;top:2330px;display:flex;gap:4px}
.dots i{width:10px;height:10px;border-radius:50%;background:var(--white)}
.dots i.off{background:transparent;border:1.5px solid var(--white)}

/* contact */
.contact{position:absolute;left:0;top:2432px;width:1200px;height:648px}
.contact-title{position:absolute;left:0;width:1186px;top:54px;text-align:center;font-size:36px;text-transform:none}
.contact-intro{position:absolute;left:220px;width:760px;top:126px;text-align:center;font-size:15px;line-height:26px}
.field{position:absolute;background:var(--field);color:var(--muted);font-size:15px;padding:16px 28px}
.contact .btn{left:141px;top:522px;width:137px;height:56px}
.touch-title{position:absolute;left:747px;top:230px;font-size:26px;text-transform:none}
.info{position:absolute;left:752px;display:flex;gap:18px;font-size:15px;line-height:26px;color:#333}
.info svg{width:17px;height:17px;fill:var(--blue);flex:none;margin-top:4px}
.social{position:absolute;width:40px;height:40px;border-radius:50%;border:1.5px solid var(--blue)}
.social.on{background:var(--blue)}

/* footer */
.footer{position:absolute;left:0;top:3080px;width:1200px;height:382px;background:radial-gradient(ellipse at 50% 40%,#23272c,var(--footer))}
.footer .brand{left:118px;top:96px}
.footer .brand-name{font-size:26px;color:var(--blue)}
.footer .brand-square{width:40px;height:40px}
.col-title{position:absolute;top:80px;font-family:"Roboto Condensed",sans-serif;font-weight:700;font-size:24px;color:var(--white)}
.links{position:absolute;top:118px;list-style:none;color:#e6e6e6;font-size:16px;line-height:30px}
.links li::before{content:"«";margin-right:12px;color:#ccc}
.news-input{position:absolute;left:813px;top:125px;width:272px;height:41px;border:1px solid #555;border-radius:22px;padding:10px 18px;color:#8d8d8d;font-size:15px}
.footer .btn{left:813px;top:177px;width:272px;height:41px}
.rule{position:absolute;left:114px;top:300px;width:972px;height:1px;background:#2d3136}
.copy{position:absolute;left:0;width:1200px;top:326px;text-align:center;color:#eee;font-size:15px}
</style>
</head>
<body>

<header class="site-header">
  <div class="brand"><div class="brand-square"></div><div class="brand-name">HARBORLINE AUTO GLASS</div></div>
  <div class="topbar">
    <span><svg viewBox="0 0 24 24"><path d="M6.6 10.8a15 15 0 0 0 6.6 6.6l2.2-2.2a1 1 0 0 1 1-.25 11.4 11.4 0 0 0 3.6.57 1 1 0 0 1 1 1V20a1 1 0 0 1-1 1A17 17 0 0 1 3 4a1 1 0 0 1 1-1h3.5a1 1 0 0 1 1 1c0 1.25.2 2.45.57 3.57a1 1 0 0 1-.25 1z"/></svg>+1 555 014 2286</span>
    <span><svg viewBox="0 0 24 24"><path d="M2 5h20v14H2z" opacity=".9"/><path d="M2 5l10 8 10-8" fill="none" stroke="#1ea3dc" stroke-width="2"/></svg>info@harborline-example.com</span>
    <span><svg viewBox="0 0 24 24"><path d="M10 17l5-5-5-5v3H2v4h8zM13 3h7v18h-7v-2h5V5h-5z"/></svg>Login</span>
  </div>
  <nav class="nav">
    <span class="active">Home</span><span>About Us</span><span>Our Services</span><span>Client Reviews</span><span>Contact Us</span>
  </nav>
</header>

<section class="hero">
  <svg width="1200" height="624" viewBox="0 0 1200 624">
    <defs>
      <linearGradient id="heroBlue" x1="0" y1="0" x2="1" y2="1">
        <stop offset="0" stop-color="#2aa9df"/><stop offset="1" stop-color="#1888c4"/>
      </linearGradient>
      <linearGradient id="heroPhoto" x1="0" y1="0" x2="1" y2="1">
        <stop offset="0" stop-color="#6e7378"/><stop offset=".5" stop-color="#3b3f47"/><stop offset="1" stop-color="#1d2026"/>
      </linearGradient>
    </defs>
    <rect x="700" y="0" width="500" height="624" fill="url(#heroPhoto)" role="img" aria-label="Technician in safety goggles fitting a new windshield onto a car"/>
    <path d="M0 0H728 C752 210 752 420 732 624H0Z" fill="url(#heroBlue)"/>
    <path d="M728 0 C752 210 752 420 732 624 L745 624 C768 420 766 210 742 0Z" fill="#1578b2"/>
    <path d="M290 520 C520 440 690 300 720 40" fill="none" stroke="#ffffff" stroke-opacity=".12" stroke-width="26"/>
  </svg>
  <h1 class="head hero-title">Welcome to<br>Harborline Auto Glass</h1>
  <p class="hero-text">Lorem ipsum dolor sit amet, consectetur adipiscing elit, sed do eiusmod tempor incididunt ut labore et dolore</p>
  <span class="btn">Schedule A Service</span>
</section>

<section class="about">
  <svg class="about-frame" width="400" height="560" viewBox="0 0 400 560">
    <defs>
      <linearGradient id="aboutPhoto" x1="0" y1="0" x2="1" y2="1">
        <stop offset="0" stop-color="#5d6168"/><stop offset=".55" stop-color="#c8463a"/><stop offset="1" stop-color="#2a2d33"/>
      </linearGradient>
    </defs>
    <path d="M60 6 L322 78 C352 220 358 380 308 500 L4 540 C48 420 70 200 60 6Z" fill="#1d76b4"/>
    <path d="M68 20 L312 86 C340 224 344 376 298 488 L18 526 C58 408 78 206 68 20Z" fill="url(#aboutPhoto)" role="img" aria-label="Gloved hands lifting glass with a red suction cup tool"/>
  </svg>
  <div class="badge"><b>24</b><i>HOURS</i></div>
  <h2 class="head about-title">About <span>Harborline Auto Glass</span></h2>
  <p class="about-text">Lorem ipsum dolor sit amet, consectetur adipiscing elit, sed do eiusmod tempor incididunt ut labore et dolore magna aliqua. Quis ipsum suspendisse ultrices gravida. Risus commodo viverra maecenas accumsan lacus vel facilisis. Lorem ipsum dolor sit amet, consectetur adipiscing elit, sed do eiusmod tempor incididunt ut labore et dolore magna aliqua. Quis ipsum suspendisse ultrices gravida. Risus commodo viverra maecenas accumsan lacus vel facilisis. Lorem ipsum dolor sit amet, consectetur adipiscing elit, sed do eiusmod tempor incididunt ut labore et dolore magna aliqua. Quis ipsum suspendisse ultrices gravida. Risus commodo viverra maecenas accumsan lacus vel facilisis. Lorem ipsum dolor sit amet, consectetur adipiscing elit, sed do eiusmod</p>
  <span class="btn">Learn More</span>
</section>

<section class="services">
  <h2 class="head services-title">Our <span>Services</span></h2>
  <div class="card" style="left:102px">
    <div class="card-pic" role="img" aria-label="Technician holding suction cups beside a windshield" style="background:linear-gradient(135deg,#9aa3ab,#c94a45 60%,#3c4249)"></div>
    <h3 class="head">Windshield Repair</h3>
    <p>Lorem ipsum dolor sit amet, consectetur adipiscing elit, sed do.</p>
    <span class="btn">Learn More</span>
  </div>
  <div class="card" style="left:356px">
    <div class="card-pic" role="img" aria-label="Hands placing a blue suction tool on windshield glass" style="background:linear-gradient(135deg,#1e2b3d,#2b6fb2 50%,#c9a083)"></div>
    <h3 class="head">Windshield Replacment</h3>
    <p>Lorem ipsum dolor sit amet, consectetur adipiscing elit, sed do.</p>
    <span class="btn">Learn More</span>
  </div>
  <div class="card" style="left:610px">
    <div class="card-pic" role="img" aria-label="Rear windshield being lifted into a car" style="background:linear-gradient(135deg,#6f8aa3,#8e9a86 50%,#3a3d40)"></div>
    <h3 class="head">Rear Windshield<br>Replacment</h3>
    <p style="top:204px;height:52px">Lorem ipsum dolor sit amet, consectetur adipisc-</p>
    <span class="btn">Learn More</span>
  </div>
  <div class="card" style="left:864px">
    <div class="card-pic" role="img" aria-label="Close view of a car side window and door" style="background:linear-gradient(135deg,#e9edf0,#a8b4bd 55%,#2f3439)"></div>
    <h3 class="head">Side Window Replacment</h3>
    <p>Lorem ipsum dolor sit amet, consectetur adipiscing elit, sed do.</p>
    <span class="btn">Learn More</span>
  </div>
</section>
<div class="arrow" style="left:43px"><svg viewBox="0 0 21 21"><path d="M12 7l-3.5 3.5L12 14" fill="none" stroke="#fff" stroke-width="1.6"/></svg></div>
<div class="arrow" style="left:1137px"><svg viewBox="0 0 21 21"><path d="M9 7l3.5 3.5L9 14" fill="none" stroke="#fff" stroke-width="1.6"/></svg></div>

<section class="reviews" role="img" aria-label="Blue-tinted background of a technician working on car glass">
  <h2 class="head reviews-title">Client Reviews<br>Harborline Auto Glass</h2>
  <h3 class="head reviewer">Morgan Ellery</h3>
  <div class="stars">
    <svg viewBox="0 0 24 24"><path d="M12 2l3 7h7l-5.5 4.5 2 7.5L12 17l-6.5 4 2-7.5L2 9h7z"/></svg>
    <svg viewBox="0 0 24 24"><path d="M12 2l3 7h7l-5.5 4.5 2 7.5L12 17l-6.5 4 2-7.5L2 9h7z"/></svg>
    <svg viewBox="0 0 24 24"><path d="M12 2l3 7h7l-5.5 4.5 2 7.5L12 17l-6.5 4 2-7.5L2 9h7z"/></svg>
    <svg viewBox="0 0 24 24"><path d="M12 2l3 7h7l-5.5 4.5 2 7.5L12 17l-6.5 4 2-7.5L2 9h7z"/></svg>
    <svg viewBox="0 0 24 24"><path d="M12 2l3 7h7l-5.5 4.5 2 7.5L12 17l-6.5 4 2-7.5L2 9h7z"/></svg>
  </div>
  <span class="quote-mark">&ldquo;</span>
  <p class="quote">Lorem ipsum dolor sit amet, consectetur adipiscing elit, sed do eiusmod tempor incididunt ut labore et dolore magna aliqua. Quis ipsum suspendisse ultrices gravida. Risus commodo viverra maecenas accumsan lacus vel facilisis. Lorem ipsum dolor sit amet, consectetur adipiscing elit, sed do eiusmod tempor incididunt ut labore et dolore magna aliqua.</p>
</section>
<div class="dots"><i></i><i class="off"></i><i></i><i></i><i></i></div>

<section class="contact">
  <h2 class="head contact-title">Contact <span>Us</span></h2>
  <p class="contact-intro">Lorem ipsum dolor sit amet, consectetur adipiscing elit, sed do eiusmod tempor incididunt ut labore et dolore magna aliqua. Quis ipsum suspendisse ultrices gravida.</p>
  <div class="field" style="left:144px;top:220px;width:255px;height:52px">First Name</div>
  <div class="field" style="left:415px;top:220px;width:255px;height:52px">Last Name</div>
  <div class="field" style="left:144px;top:288px;width:255px;height:51px">Email</div>
  <div class="field" style="left:415px;top:288px;width:254px;height:51px">Phone</div>
  <div class="field" style="left:144px;top:355px;width:525px;height:141px">Messages</div>
  <span class="btn">Submit</span>

  <h3 class="head touch-title">Get&nbsp; in <span>Touch</span></h3>
  <div class="info" style="top:296px"><svg viewBox="0 0 24 24"><path d="M12 2a7 7 0 0 0-7 7c0 5 7 13 7 13s7-8 7-13a7 7 0 0 0-7-7zm0 9.5A2.5 2.5 0 1 1 12 6.5a2.5 2.5 0 0 1 0 5z"/></svg><span>199 /b Harborline Auto Glass consectetur<br>adipiscing elit, sed do eiusmod tempor</span></div>
  <div class="info" style="top:360px"><svg viewBox="0 0 24 24"><path d="M6.6 10.8a15 15 0 0 0 6.6 6.6l2.2-2.2a1 1 0 0 1 1-.25 11.4 11.4 0 0 0 3.6.57 1 1 0 0 1 1 1V20a1 1 0 0 1-1 1A17 17 0 0 1 3 4a1 1 0 0 1 1-1h3.5a1 1 0 0 1 1 1c0 1.25.2 2.45.57 3.57a1 1 0 0 1-.25 1z"/></svg><span>+1 555 014 2286</span></div>
  <div class="info" style="top:402px"><svg viewBox="0 0 24 24"><path d="M2 5h20v14H2z"/><path d="M2 5l10 8 10-8" fill="none" stroke="#fff" stroke-width="2"/></svg><span>info@harborline-example.com</span></div>
  <div class="social on" style="left:749px;top:459px" aria-label="Social profile"></div>
  <div class="social" style="left:797px;top:459px" aria-label="Social profile"></div>
  <div class="social" style="left:847px;top:459px" aria-label="Social profile"></div>
  <div class="social" style="left:896px;top:459px" aria-label="Social profile"></div>
</section>

<footer class="footer">
  <div class="brand"><div class="brand-square"></div><div class="brand-name">HARBORLINE<br>AUTO GLASS</div></div>
  <div class="col-title" style="left:407px">Quick Link</div>
  <ul class="links" style="left:410px"><li>Home</li><li>About Us</li><li>Our Services</li><li>Client Reviews</li><li>Contact Us</li></ul>
  <div class="col-title" style="left:598px">Help Link</div>
  <ul class="links" style="left:598px"><li>Terms&amp;Conditions</li><li>Privacy Policy</li><li>About Us</li><li>Support</li></ul>
  <div class="col-title" style="left:813px">Get Our Newsletter</div>
  <div class="news-input">Enter Your Email</div>
  <span class="btn">Subscribe Now</span>
  <div class="rule"></div>
  <p class="copy">&copy;Copyrights 2022 Harborline Auto Glass |&nbsp;&nbsp; All Rights Reserved</p>
</footer>

</body>
</html>
```